依頼詳細
ターゲット層が50代以上になる予想ですので、ネットよりチラシの方が分かりやすいと思っております。

イメージしているチラシは下記に貼っときますのでご確認ください。
デザインイメージとしては、
・明るいチラシ
・カテゴリー分けされた分かりやすいチラシ
・チラシ保管による割引
割引内容(5000円以上で500円引き、10000円以上で1000円引き)
・一目でわかる大きな不用品回収、買取の文言
・ビフォー、アフターの写真を掲載
・自社キャラクターの添付(下記に添付しております)
・キャラクターでわかりやすいスケジュールの流れ
・回収、買取実績の値段詳細を掲載(数字はこちらで記載するので空欄でも大丈夫です。¥00,000~と入れていただけばと思います。)

以上多くなりましたがこちらをできるだけ加えて作成して頂くと幸いです。
細か点や、不明点が生じると思います。お気軽にご質問下さい。
よろしくお願い致します。
記載項目
社名:売りナビ福岡天神店/電話番号:0120-47-3286/HP:https://urinavi-example.jp/area/fukuokatenjin//住所:〒812-4093 福岡県糟屋郡粕屋町桜見台東3丁目8−24
サイズ
B4
ページ数
両面
希望イメージ
シンプル 複雑
単色 カラフル
暗い 明るい
日常 高級
遊び心 厳粛
未来的 伝統的
女性的 男性的
希望する色
設定なし
納品ファイル
• イラストレーター形式 (.ai)
補足説明
自社キャラクターの横にこの方が行きますみたいな吹き出しを入れて頂きたいです。

添付資料の1枚目、2枚目が理想に近いです。
こちらにできるだけ近づけて頂いたらと思います。
よろしくお願い致します。

イメージに一番近く最高な出来でした。

皆様この度はご提案いただき誠に有難うございます。
今後また、依頼することあればよろしくお願い致します。

森下

```html
<!DOCTYPE html>
<html lang="ja">
<head>
<meta charset="utf-8">
<title>売りナビ福岡天神店 不用品 買取・回収 チラシ</title>
<link href="https://fonts.googleapis.com/css2?family=Noto+Sans+JP:wght@400;700;900&family=M+PLUS+Rounded+1c:wght@700;800&display=swap" rel="stylesheet">
<style>
:root{
  --yellow:#ffd800;
  --black:#1a1a1a;
  --red:#e60012;
  --purple:#4b2a7b;
  --green:#8dc21f;
  --sky:#2ea7e0;
  --cream:#fff8d6;
  --white:#ffffff;
  --grey:#6d6d6d;
}
*{margin:0;padding:0;box-sizing:border-box}
html,body{width:846px;height:1200px;overflow:hidden;background:var(--white)}
body{font-family:"Noto Sans JP",sans-serif;color:var(--black);position:relative}
.flyer{position:absolute;inset:0;overflow:hidden}

.header{position:absolute;left:0;top:0;width:846px;height:490px;background:var(--yellow)}
.title{position:absolute;left:30px;top:18px;font-weight:900;font-size:178px;line-height:1;letter-spacing:-4px}
.service{position:absolute;left:30px;font-weight:900;line-height:1;font-size:88px;letter-spacing:2px}
.service--buy{top:215px}
.service--estate{top:310px}
.badge{position:absolute;left:640px;top:32px;width:180px;height:180px;border-radius:50%;background:var(--purple);color:var(--white);display:flex;align-items:center;justify-content:center;transform:rotate(-12deg);font-family:"M PLUS Rounded 1c",sans-serif;font-weight:800;font-size:30px;line-height:1.2;text-align:center;z-index:2}
.mascot{position:absolute;left:470px;top:165px;width:220px;height:270px;border-radius:110px 110px 30px 30px;background:linear-gradient(#f5c7a0,#f1e6cc)}
.speech{position:absolute;left:782px;top:300px;writing-mode:vertical-rl;font-size:20px;font-weight:700;color:var(--purple)}

.ba-label{position:absolute;top:505px;font-size:36px;font-weight:700;font-family:"M PLUS Rounded 1c",sans-serif;line-height:1.2}
.photo{position:absolute;top:555px;height:135px}
.photo--before{left:14px;width:280px;background:linear-gradient(#c7b08a,#8c7457)}
.photo--after{left:312px;width:268px;background:linear-gradient(#f2efe9,#b58d62)}

.free{position:absolute;left:606px;top:505px;width:204px;height:100px;border:4px solid var(--red);border-radius:10px;color:var(--red);text-align:center;font-weight:900;font-size:30px;line-height:1.25;padding-top:6px}
.free span{display:block;background:var(--red);color:var(--white);font-size:38px;line-height:1.2;margin:6px 8px 0;border-radius:4px}
.movers{position:absolute;left:606px;top:614px;width:204px;height:96px;background:linear-gradient(#9ec9e6,#e9d5b0)}
.onsite{position:absolute;left:596px;top:716px;width:226px;text-align:center;font-weight:900;line-height:1.3}
.onsite .small{display:block;font-size:17px}
.onsite .big{display:block;font-size:30px;color:var(--red);border-bottom:3px solid var(--red);line-height:1.15}
.onsite .note{display:block;font-size:15px;font-weight:700;margin-top:2px}

.record{position:absolute;left:14px;top:700px;width:570px;border-top:3px solid var(--black)}
.record-head{display:flex;align-items:center;gap:14px;height:50px}
.consult{width:104px;color:var(--red);font-weight:900;font-size:16px;line-height:1.3;text-align:center}
.record h2{font-size:16px;font-weight:700}
.record table{width:100%;border-collapse:collapse;font-size:15px}
.record td{height:30px;padding:0 8px;border-bottom:1px solid var(--grey)}
.record td.price{text-align:right;font-weight:700}

.steps{position:absolute;left:14px;top:818px;width:570px;height:145px;display:flex;gap:12px}
.step{flex:1;position:relative;background:var(--cream);border-radius:8px;padding:8px 8px 0 42px;font-size:13px;font-weight:700;line-height:1.35}
.step .num{position:absolute;left:6px;top:6px;width:30px;height:30px;border-radius:50%;background:var(--black);color:var(--white);display:flex;align-items:center;justify-content:center;font-size:18px}
.step .scene{position:absolute;left:8px;right:8px;bottom:8px;height:66px;border-radius:6px;background:linear-gradient(#cfe6f4,#f3d9b6)}

.deal{position:absolute;left:590px;top:818px;width:250px;text-align:center;font-size:16px;font-weight:900;color:var(--purple);line-height:1.5}
.deal b{color:var(--red);font-size:21px}
.coupon{position:absolute;left:596px;width:236px;height:95px;border:2px dashed var(--black);display:flex}
.coupon--500{top:852px;background:var(--yellow)}
.coupon--1000{top:962px;background:var(--green)}
.coupon .body{flex:1;text-align:center;padding-top:8px;font-weight:700;font-size:14px}
.coupon .amount{display:block;font-size:44px;font-weight:900;line-height:1.1}
.coupon .amount small{font-size:20px}
.coupon .tag{width:30px;background:var(--sky);color:var(--white);writing-mode:vertical-rl;font-size:13px;font-weight:700;display:flex;align-items:center;justify-content:center;letter-spacing:2px}

.contact{position:absolute;left:14px;top:978px;width:570px}
.phone{display:flex;align-items:center;gap:8px;color:var(--red);font-weight:900;font-size:54px;line-height:1.1}
.shop{font-size:26px;font-weight:900;margin-top:8px;line-height:1.3}
.address,.web{font-size:15px;font-weight:700;margin-top:6px;line-height:1.4}
</style>
</head>
<body>
<div class="flyer">
  <section class="header">
    <h1 class="title">不用品</h1>
    <p class="service service--buy">買取 回収</p>
    <p class="service service--estate">遺品整理</p>
    <div class="mascot" role="img" aria-label="自社キャラクターのイラスト"></div>
    <div class="badge">プロに<br>お任せ<br>下さい</div>
    <p class="speech">僕が行きます</p>
  </section>

  <p class="ba-label" style="left:50px">Before</p>
  <p class="ba-label" style="left:340px">After</p>
  <div class="photo photo--before" role="img" aria-label="片付け前の部屋の写真"></div>
  <div class="photo photo--after" role="img" aria-label="片付け後のきれいな部屋の写真"></div>

  <div class="free">お見積り<span>無料</span></div>
  <div class="movers" role="img" aria-label="作業スタッフのイラスト"></div>
  <p class="onsite"><span class="small">その場で</span><span class="big">即見積・即回収</span><span class="note">お気軽にご相談下さい！</span></p>

  <div class="record">
    <div class="record-head">
      <p class="consult">一か所から<br>お気軽に</p>
      <h2>回収 買取実績の値段詳細</h2>
    </div>
    <table>
      <tr><td>1Rームまるごとパック</td><td class="price">¥00,000~</td></tr>
      <tr><td>2DKまるごとパック</td><td class="price">¥00,000~</td></tr>
    </table>
  </div>

  <div class="steps">
    <div class="step"><span class="num">1</span>まずはフリーダイヤルにお電話を<div class="scene" role="img" aria-label="電話をかけるイラスト"></div></div>
    <div class="step"><span class="num">2</span>回収<br>お片付け<div class="scene" role="img" aria-label="回収作業のイラスト"></div></div>
    <div class="step"><span class="num">3</span>お見積り・ご相談は無料です<div class="scene" role="img" aria-label="見積りのイラスト"></div></div>
  </div>

  <p class="deal">今ならお得な<b>割引</b>ございます</p>
  <div class="coupon coupon--500"><div class="body">5000円以上で<span class="amount">500<small>円引き</small></span></div><div class="tag">COUPON</div></div>
  <div class="coupon coupon--1000"><div class="body">10000円以上で<span class="amount">1000<small>円引き</small></span></div><div class="tag">COUPON</div></div>

  <div class="contact">
    <p class="phone"><svg width="46" height="46" viewBox="0 0 24 24" aria-hidden="true"><path fill="currentColor" d="M6.6 10.8a15 15 0 0 0 6.6 6.6l2.2-2.2c.3-.3.7-.4 1-.2 1.1.4 2.3.6 3.6.6.6 0 1 .4 1 1V20c0 .6-.4 1-1 1A17 17 0 0 1 3 4c0-.6.4-1 1-1h3.5c.6 0 1 .4 1 1 0 1.3.2 2.5.6 3.6.1.3 0 .7-.2 1z"/></svg>0120-47-3286</p>
    <p class="shop">売りナビ福岡天神店</p>
    <p class="address">住所：〒812-4093 福岡県糟屋郡粕屋町桜見台東3丁目8−24</p>
    <p class="web">HP:https://urinavi-example.jp/area/fukuokatenjin/</p>
  </div>
</div>
</body>
</html>
```